New energy tablet requires a logo / packaging design

We need a logo designed for a new energy tablet (capsule) called "Vo-Lumo". We would like to see designs that communicate a fun, youthful brand aimed primarily at a demographic of 18 - 35.

This will be a herbal energy tablet to be sold online to to people looking to increase energy and mood lifts.

We do have a previous design that we used before and would like that one to be used again but just revamped a little to give it a fresher look and more depth to the design if possible.

Completely new designs are also welcome if you would prefer but ideally we want it to look as similar to the original one as possible.

We are committed to payment on this design.

Thank you all in advance for your design submissions.

These are to be printed onto black foil zip seal bags to contain 1 pellet only.

Target Market(s)

customers that visit online and high street shops that sell herbal energy products

Industry/Entity Type

Online

Requirements
Must have
• Must have the words VO-LUMO and PELLET in the logo design

```html
<!DOCTYPE html>
<html lang="en">
<head>
<meta charset="utf-8">
<title>Vo-Lumo Pellet – Energy Tablet Label</title>
<link rel="stylesheet" href="https://fonts.googleapis.com/css2?family=Roboto+Condensed:wght@500;700&display=swap">
<style>
  :root {
    --stage: #ececec;
    --label-teal: #01a78e;
    --panel-dark: #04161a;
    --panel-mid: #0d4a52;
    --frame-light: #d9dfe0;
    --frame-dark: #7d8788;
    --name-cyan: #86e6e8;
    --accent-teal: #14b39a;
    --pill-dark: #1e1e1e;
    --ink: #222222;
    --white: #ffffff;
  }
  html, body {
    margin: 0;
    padding: 0;
    width: 1200px;
    height: 1000px;
    overflow: hidden;
    background: var(--stage);
  }
  .label {
    position: absolute;
    left: 200px;
    top: 78px;
    width: 800px;
    height: 845px;
    background: var(--label-teal);
    font-family: "Roboto Condensed", "Arial Narrow", sans-serif;
  }
  .label__panel {
    position: absolute;
    left: 0;
    top: 0;
    width: 800px;
    height: 700px;
  }
  .brand {
    position: absolute;
    left: 0;
    width: 800px;
    top: 380px;
    text-align: center;
  }
  .brand__name {
    margin: 0;
    font-weight: 700;
    font-size: 112px;
    line-height: 1;
    letter-spacing: 2px;
    color: var(--name-cyan);
  }
  .brand__variant {
    margin: 14px 0 0;
    font-weight: 700;
    font-size: 34px;
    line-height: 1;
    letter-spacing: 1px;
    color: var(--white);
  }
  .supplement-note {
    position: absolute;
    left: 0;
    width: 800px;
    top: 640px;
    margin: 0;
    text-align: center;
    font-weight: 500;
    font-size: 24px;
    color: var(--accent-teal);
  }
  .product-pill {
    position: absolute;
    left: 170px;
    top: 709px;
    width: 458px;
    height: 57px;
    border-radius: 29px;
    background: var(--pill-dark);
    color: var(--white);
    font-weight: 700;
    font-size: 38px;
    line-height: 57px;
    text-align: center;
    margin: 0;
  }
  .capsule-count {
    position: absolute;
    left: 0;
    width: 800px;
    top: 778px;
    margin: 0;
    text-align: center;
    font-weight: 700;
    font-size: 24px;
    color: var(--ink);
  }
</style>
</head>
<body>
  <main class="label">
    <svg class="label__panel" viewBox="0 0 800 700" aria-hidden="true">
      <defs>
        <linearGradient id="frameMetal" x1="0" y1="0" x2="1" y2="1">
          <stop offset="0" stop-color="var(--frame-dark)"/>
          <stop offset="0.45" stop-color="var(--frame-light)"/>
          <stop offset="1" stop-color="var(--frame-dark)"/>
        </linearGradient>
        <linearGradient id="panelGlow" x1="0" y1="0" x2="0" y2="1">
          <stop offset="0" stop-color="#000000"/>
          <stop offset="0.08" stop-color="var(--panel-dark)"/>
          <stop offset="0.5" stop-color="var(--panel-mid)"/>
          <stop offset="0.78" stop-color="#0a3238"/>
          <stop offset="1" stop-color="#030c0e"/>
        </linearGradient>
      </defs>
      <path class="panel-frame" d="M114 0 H686 V620 L594 700 H206 L114 620 Z" fill="url(#frameMetal)"/>
      <path class="panel-body" d="M125 0 H675 V615 L589 689 H211 L125 615 Z" fill="url(#panelGlow)"/>
      <rect class="panel-top-band" x="125" y="0" width="550" height="52" fill="#000000"/>
    </svg>

    <div class="brand">
      <h1 class="brand__name">VO-LUMO</h1>
      <p class="brand__variant">PELLET</p>
    </div>

    <p class="supplement-note">DIETARY SUPPLEMENT</p>
    <p class="product-pill">ENERGY TABLET</p>
    <p class="capsule-count">120 CAPSULES VEGETARIAN</p>
  </main>
</body>
</html>
```